Silver Meadow Dove Release Website Deisgn project

We need a website design for our dove release business.

We had several business cards designed awhile back....one for weddings and one for general releases (usually funerals). It was so hard to pick from all the great designs that were submitted. I have attached them.

We release white doves for all celebrations in life. Weddings, funerals, store openings, remembrance ceremonies, etc.

We need to appeal to brides and grooms as well as those grieving the loss of a loved one. It's a very delicate blend.

The name of our business is "Silver Meadow" and the name of our loft is "Tarn's Roost". Our loft was established in 2012.

Target Market(s)

Brides, Grooms, Grieving Adults, Wedding Planners, Funeral Homes, Promoters

Industry/Entity Type

Professional Service

Number of Pages Required

5+ page

Font styles to use
Sans Serif

Requirements
Must have
• We will need some space for pictures I'm sure. We will need to have a contract & pricing page. We will need a contact us page.
• We need a more classic feel as we need to attract brides and those who are grieving. The solution may be a page for each......Wedding Releases & Funeral Releases & Other Celebrations
Nice to have
• If we have a page for each type of life celebration, there's more options for color. I would like the designer to choose the colors that are appropriate for the occasion.
• I would like to have a bit of decorative font in addition to the traditional website font.
Should not have
• We need to stay away from the yellow and orange colors.

```html
<!DOCTYPE html>
<html lang="en">
<head>
<meta charset="utf-8">
<title>Silver Meadow — Dove Releases</title>
<link rel="stylesheet" href="https://fonts.googleapis.com/css2?family=Yanone+Kaffeesatz:wght@400;500&family=PT+Sans:wght@400;700&display=swap">
<style>
:root{
  --red:#e01f26;
  --red-dark:#b3151b;
  --charcoal:#333333;
  --charcoal-deep:#252525;
  --white:#ffffff;
  --text:#555555;
  --bg-pink:#f6e8ea;
  --heading:"Yanone Kaffeesatz", sans-serif;
  --body:"PT Sans", sans-serif;
}
*{margin:0;padding:0;box-sizing:border-box}
html,body{width:1015px;height:1200px;overflow:hidden}
body{
  background-color:var(--bg-pink);
  background-image:radial-gradient(circle,#fdf7f8 2px,transparent 2.5px);
  background-size:18px 18px;
  font-family:var(--body);
  position:relative;
}
.page{position:absolute;left:71px;top:0;width:873px;height:1200px;background:var(--white)}

/* Header */
.site-header{position:absolute;left:0;top:0;width:873px;height:120px;background:var(--charcoal)}
.contact-chip{position:absolute;top:43px;display:flex;align-items:center;gap:10px;color:#f1f1f1;font-size:13.6px}
.contact-chip.phone{left:25px}
.contact-chip.email{right:27px}
.chip-icon{width:34px;height:34px;border-radius:50%;background:var(--red);border:2px solid #232323;box-shadow:0 0 0 2px #444;display:flex;align-items:center;justify-content:center}
.brand{position:absolute;left:0;right:0;top:44px;text-align:center;color:var(--white)}
.brand-name{font-family:var(--heading);font-size:38px;font-weight:400;letter-spacing:1px;line-height:1}
.brand-tag{font-family:var(--body);font-size:6px;margin-top:6px;padding:3px 0;border-top:1px solid #bbb;border-bottom:1px solid #bbb;display:inline-block;width:126px}

/* Nav */
.main-nav{position:absolute;left:-15px;top:120px;width:903px;height:57px;background:linear-gradient(#e4252b,#c8171d)}
.main-nav::before,.main-nav::after{content:"";position:absolute;bottom:-11px;border-top:11px solid var(--red-dark)}
.main-nav::before{left:0;border-left:11px solid transparent}
.main-nav::after{right:0;border-right:11px solid transparent}
.nav-link{position:absolute;top:0;line-height:57px;font-family:var(--heading);font-size:14.5px;color:var(--white);text-decoration:none;transform:translateX(-50%);letter-spacing:.3px;white-space:nowrap}
.nav-link.active{top:15px;height:28px;line-height:28px;width:63px;text-align:center;background:var(--charcoal-deep);clip-path:polygon(6px 0,calc(100% - 6px) 0,100% 50%,calc(100% - 6px) 100%,6px 100%,0 50%)}

/* Hero */
.hero{position:absolute;left:0;top:177px;width:873px;height:396px}
.hero-photo{position:absolute;left:0;top:0;width:873px;height:289px;background:linear-gradient(170deg,#9aa2ad 0%,#c9ccd0 35%,#e6e7e8 48%,#8e969e 62%,#3f5138 82%,#233421 100%)}
.hero-arrows{position:absolute;left:767px;top:260px;display:flex;gap:4px}
.hero-arrow{width:41px;height:29px;background:#222;display:flex;align-items:center;justify-content:center}
.hero-caption{position:absolute;left:0;top:289px;width:873px;height:107px;background:rgba(214,27,36,.93);padding:22px 22px 0;color:var(--white)}
.hero-title{font-family:var(--heading);font-size:31px;font-weight:400;letter-spacing:.5px;line-height:1}
.hero-text{font-size:9.9px;line-height:17.5px;margin-top:4px}

/* Services */
.services{position:absolute;left:23px;top:602px;display:flex;gap:22px}
.service-card{width:190px;height:160px;position:relative}
.service-photo{width:190px;height:125px}
.service-label{position:absolute;left:0;bottom:0;width:190px;height:44px;background:linear-gradient(#3a3a3a,#272727);color:var(--white);font-family:var(--heading);font-size:20px;text-align:center;line-height:44px;letter-spacing:.5px;clip-path:polygon(4px 0,calc(100% - 4px) 0,100% 8px,100% 100%,0 100%,0 8px)}

/* Feature */
.feature{position:absolute;left:23px;top:804px;width:474px}
.feature-title{font-family:var(--heading);font-size:26px;font-weight:400;color:#2c2c2c;letter-spacing:.5px;line-height:1}
.feature-text{font-size:9.6px;line-height:21.8px;color:var(--text);margin-top:10px;text-align:justify}
.btn-read{position:absolute;left:0;top:159px;width:148px;height:44px;background:var(--red);color:var(--white);font-family:var(--heading);font-size:20px;text-align:center;line-height:44px;text-decoration:none;clip-path:polygon(8px 0,calc(100% - 8px) 0,100% 8px,calc(100% - 4px) 50%,100% calc(100% - 8px),calc(100% - 8px) 100%,8px 100%,0 calc(100% - 8px),4px 50%,0 8px)}
.feature-frame{position:absolute;left:518px;top:806px;width:332px;height:200px;border:1px solid #ddd;padding:3px;background:var(--white);box-shadow:0 0 2px rgba(0,0,0,.15)}
.feature-photo{width:100%;height:100%;background:linear-gradient(90deg,#cdb896 0%,#e9dcc4 22%,#f7f1e6 50%,#d7c3a4 70%,#3c3128 82%,#8d7a62 100%)}

/* Contact band */
.contact-band{position:absolute;left:0;top:1044px;width:873px;height:82px;background:var(--red);display:flex;align-items:center;justify-content:center;gap:16px;color:var(--white);font-size:22px}
.band-item{display:flex;align-items:center;gap:13px}
.band-icon{width:49px;height:49px;border-radius:50%;background:#1e1e1e;display:flex;align-items:center;justify-content:center}

/* Footer */
.site-footer{position:absolute;left:0;top:1126px;width:873px;height:74px;background:var(--charcoal);color:#e6e6e6;font-size:8.6px;padding:17px 0 0 23px;line-height:21px}
.social{position:absolute;right:22px;top:28px;display:flex;gap:5px}
.social span{width:17px;height:17px;border-radius:50%}
</style>
</head>
<body>
<div class="page">
  <header class="site-header">
    <div class="contact-chip phone">
      <span class="chip-icon"><svg width="14" height="14" viewBox="0 0 24 24"><path fill="#fff" d="M6.6 10.8a15.1 15.1 0 0 0 6.6 6.6l2.2-2.2c.3-.3.7-.4 1-.2 1.1.4 2.3.6 3.6.6.6 0 1 .4 1 1V20c0 .6-.4 1-1 1A17 17 0 0 1 3 4c0-.6.4-1 1-1h3.5c.6 0 1 .4 1 1 0 1.3.2 2.5.6 3.6.1.3 0 .7-.2 1z"/></svg></span>
      612-555-0147
    </div>
    <div class="brand">
      <div class="brand-name">SILVER MEADOW</div>
      <div class="brand-tag">Doves provided by Tarn's Roost (est. 2012)</div>
    </div>
    <div class="contact-chip email">
      silvermeadow2012@mailbox.com
      <span class="chip-icon"><svg width="14" height="12" viewBox="0 0 24 20"><path fill="#fff" d="M2 2h20v2l-10 7L2 4z M2 7l10 7 10-7v11H2z"/></svg></span>
    </div>
  </header>

  <nav class="main-nav">
    <a class="nav-link active" href="#" style="left:247px">HOME</a>
    <a class="nav-link" href="#" style="left:353px">ABOUT US</a>
    <a class="nav-link" href="#" style="left:460px">SERVICES</a>
    <a class="nav-link" href="#" style="left:566px">EVENTS</a>
    <a class="nav-link" href="#" style="left:668px">GALLERY</a>
    <a class="nav-link" href="#" style="left:783px">CONTACT US</a>
  </nav>

  <section class="hero">
    <div class="hero-photo" role="img" aria-label="Two white doves in flight against a grey sky above a pine forest"></div>
    <div class="hero-arrows">
      <span class="hero-arrow"><svg width="10" height="14" viewBox="0 0 10 14"><path d="M8 1 2 7l6 6" stroke="#fff" stroke-width="2" fill="none"/></svg></span>
      <span class="hero-arrow"><svg width="10" height="14" viewBox="0 0 10 14"><path d="m2 1 6 6-6 6" stroke="#fff" stroke-width="2" fill="none"/></svg></span>
    </div>
    <div class="hero-caption">
      <h1 class="hero-title">SILVER MEADOW</h1>
      <p class="hero-text">Lorem ipsum dolor sit amet, consectetur adipiscing elit. Nullam euismod lacinia sodales. Pellentesque luctus elit a ipsum volutpat, ut mattis mi bibendum. Sed ac diam sed felis vulputate ornare. Phasellus ac tempor orci. Proin luctus vel neque at hendrerit. Cras sed leo ornare ligula aliquam tempor.</p>
    </div>
  </section>

  <section class="services">
    <div class="service-card">
      <div class="service-photo" role="img" aria-label="Wedding couple greeting a guest in a garden" style="background:linear-gradient(160deg,#8db25a 0%,#c8d9a0 30%,#e8e6dc 50%,#4a525e 75%,#2e333b 100%)"></div>
      <div class="service-label">WEDDINGS</div>
    </div>
    <div class="service-card">
      <div class="service-photo" role="img" aria-label="Mourners gathered at a funeral with red and yellow flowers" style="background:linear-gradient(180deg,#b7c0c4 0%,#4b4d52 30%,#1f1f23 60%,#c8281e 85%,#e0a21c 100%)"></div>
      <div class="service-label">FUNERALS</div>
    </div>
    <div class="service-card">
      <div class="service-photo" role="img" aria-label="Scissors cutting a red ribbon at a store opening" style="background:linear-gradient(160deg,#7f8a96 0%,#c9c9cb 35%,#d6242a 55%,#2f3540 80%,#1e2228 100%)"></div>
      <div class="service-label">STORE OPENINGS</div>
    </div>
    <div class="service-card">
      <div class="service-photo" role="img" aria-label="Lit remembrance candles glowing in the dark" style="background:linear-gradient(180deg,#1a0804 0%,#8a3410 35%,#f0a23a 55%,#c82a1c 80%,#8f1410 100%)"></div>
      <div class="service-label">REMEMBRANCE</div>
    </div>
  </section>

  <section class="feature">
    <h2 class="feature-title">APPEAL TO BRIDES AND GROOMS</h2>
    <p class="feature-text">Morbi interdum ultricies ipsum, vel imperdiet nunc tincidunt a. Nunc consequat condimentum egestas. Nullam odio urna, auctor in elementum ut, fermentum vel libero. Nulla felis purus, vehicula eu sagittis ut, interdum non nisl. Curabitur sed justo at augue ornare feugiat. Sed vitae consectetur nisl, id tincidunt ante. Donec aliquet maximus augue, eu volutpat lectus mattis eget. Nullam molestie erat sed facilisis porttitor. Integer varius vitae quam quis placerat. Sed erat ex, mollis non diam et, scelerisque fringilla sem.</p>
    <a class="btn-read" href="#">READ MORE</a>
  </section>
  <div class="feature-frame">
    <div class="feature-photo" role="img" aria-label="Bride adjusting the groom's tie by a sunlit window"></div>
  </div>

  <section class="contact-band">
    <div class="band-item">
      <span class="band-icon"><svg width="24" height="24" viewBox="0 0 24 24"><path fill="#fff" d="M6.6 10.8a15.1 15.1 0 0 0 6.6 6.6l2.2-2.2c.3-.3.7-.4 1-.2 1.1.4 2.3.6 3.6.6.6 0 1 .4 1 1V20c0 .6-.4 1-1 1A17 17 0 0 1 3 4c0-.6.4-1 1-1h3.5c.6 0 1 .4 1 1 0 1.3.2 2.5.6 3.6.1.3 0 .7-.2 1z"/></svg></span>
      612-555-0147
    </div>
    <div class="band-item">
      <span class="band-icon"><svg width="22" height="18" viewBox="0 0 24 20"><path fill="#fff" d="M2 2h20v2l-10 7L2 4z M2 7l10 7 10-7v11H2z"/></svg></span>
      silvermeadow2012@mailbox.com
    </div>
  </section>

  <footer class="site-footer">
    <div>Privacy Policy &nbsp;|&nbsp; Sitemap</div>
    <div>Copyright © 2016 Silver Meadow. All rights reserved</div>
    <div class="social" aria-label="Social links">
      <span style="background:#3b5a9a"></span>
      <span style="background:#2fa9e0"></span>
      <span style="background:#1a7bb0"></span>
      <span style="background:#d4322a"></span>
      <span style="background:#f08a24"></span>
      <span style="background:#d9483b"></span>
    </div>
  </footer>
</div>
</body>
</html>
```